Ninety Truths Gathered Across Four Decades Advising Firms

I need the design for my book cover, plus the spine and the back cover. I need this for both a hard cover book and an ebook

Target Market(s)

Any person in business with managerial responsibility

Industry/Entity Type

Consulting

Font styles to use
Serif

Requirements
Must have
• Must look very professional. No script/cursive is to be used. The cover should be clean, not cluttered.so the title really stands out well
Nice to have
• A professional image to reinforce the title
Should not have
• Script, cartoons or anything that does not look professional

```html
<!DOCTYPE html>
<html lang="en">
<head>
<meta charset="utf-8">
<title>Ninety Truths Gathered Across Four Decades Advising Firms — Book Cover</title>
<link rel="stylesheet" href="https://fonts.googleapis.com/css2?family=Bebas+Neue&family=Montserrat:wght@300;400&display=swap">
<style>
  :root {
    --stage: #e6e6e6;
    --cover-top: #0d1f33;
    --cover-mid: #081626;
    --cover-bottom: #040b16;
    --title-cyan: #1ea9e8;
    --title-yellow: #f7ee00;
    --text-white: #ffffff;
    --photo-blue: #1d3d5e;
    --photo-deep: #0a1a2c;
    --photo-skin: #b77b62;
  }
  * { margin: 0; padding: 0; box-sizing: border-box; }
  html, body {
    width: 1200px;
    height: 800px;
    overflow: hidden;
    background: var(--stage);
  }
  .canvas {
    width: 1200px;
    height: 800px;
    display: flex;
    align-items: center;
    justify-content: center;
  }
  .book-cover {
    position: relative;
    width: 546px;
    height: 722px;
    background: linear-gradient(180deg, var(--cover-top) 0%, var(--cover-mid) 45%, var(--cover-bottom) 100%);
    overflow: hidden;
    text-align: center;
    color: var(--text-white);
  }
  .title-block {
    position: absolute;
    top: 38px;
    left: 0;
    right: 0;
  }
  .title-line {
    font-family: "Bebas Neue", "Oswald", sans-serif;
    font-size: 84px;
    line-height: 0.9;
    letter-spacing: 1px;
  }
  .title-line--cyan { color: var(--title-cyan); }
  .title-line--yellow { color: var(--title-yellow); }
  .subtitle-rule {
    display: flex;
    align-items: center;
    justify-content: center;
    gap: 18px;
    margin: 8px 0 10px;
    font-family: "Montserrat", Arial, sans-serif;
    font-weight: 300;
    font-size: 23px;
    letter-spacing: 0.5px;
  }
  .subtitle-rule::before,
  .subtitle-rule::after {
    content: "";
    width: 52px;
    height: 4px;
    background: var(--text-white);
  }
  .spaced-word {
    margin-top: 10px;
    font-family: "Montserrat", Arial, sans-serif;
    font-weight: 400;
    font-size: 25px;
    letter-spacing: 11px;
    padding-left: 11px;
  }
  .cover-photo {
    position: absolute;
    top: 270px;
    left: 0;
    width: 546px;
    height: 360px;
    display: block;
  }
  .author-name {
    position: absolute;
    bottom: 26px;
    left: 0;
    right: 0;
    font-family: "Bebas Neue", "Oswald", sans-serif;
    font-size: 33px;
    letter-spacing: 0.5px;
  }
</style>
</head>
<body>
<main class="canvas">
  <section class="book-cover">
    <header class="title-block">
      <h1 class="title-line title-line--cyan">Ninety Truths</h1>
      <p class="subtitle-rule">GATHERED ACROSS</p>
      <p class="title-line title-line--yellow">Four Decades</p>
      <p class="spaced-word">ADVISING FIRMS</p>
    </header>

    <svg class="cover-photo" viewBox="0 0 546 360" role="img"
         aria-label="Photo of a businessman in a dark suit holding cupped hands, with a small group of glowing white business figures standing on his palms">
      <defs>
        <radialGradient id="photoGlow" cx="50%" cy="45%" r="60%">
          <stop offset="0%" stop-color="var(--photo-blue)"/>
          <stop offset="60%" stop-color="var(--photo-deep)"/>
          <stop offset="100%" stop-color="var(--cover-mid)" stop-opacity="0"/>
        </radialGradient>
        <radialGradient id="handsTone" cx="50%" cy="75%" r="35%">
          <stop offset="0%" stop-color="var(--photo-skin)" stop-opacity="0.55"/>
          <stop offset="100%" stop-color="var(--photo-skin)" stop-opacity="0"/>
        </radialGradient>
      </defs>
      <rect width="546" height="360" fill="url(#photoGlow)"/>
      <rect width="546" height="360" fill="url(#handsTone)"/>
    </svg>

    <p class="author-name">AUTHOR NAME</p>
  </section>
</main>
</body>
</html>
```